shop signs for newquay all year round

We require a shop front signage
2 x 2.5m Long by 1.5m High (sides)
1 x 8m long by 0.7m High (front)

The front sign must read - Penny Wise Bargain Store with the last 1.5m showing the the Xmas Shop open all year (see image 1)

The side signs must have a big bold Arrow pointing Left and one Pointing Right with the words Clearance Sale Now On (see image 2)

Colors

Designer to choose colors to be used in the design.

Requirements
Must have
• signs must be bold and clear to get shoppers into the store, it must be bright and stand out
Nice to have
• good graphics and artwork
Should not have
• plain text

```html
<!DOCTYPE html>
<html lang="en">
<head>
<meta charset="utf-8">
<title>Penny Wise Bargain Store – Front Sign</title>
<link rel="stylesheet" href="https://fonts.googleapis.com/css2?family=Bebas+Neue&family=Almendra+Display&display=swap">
<style>
  :root {
    --page: #6b6b6b;
    --sky-light: #95c8dc;
    --sky-deep: #55a0be;
    --snow: #ffffff;
    --headline: #ffffff;
    --accent-red: #e8302f;
    --tree-green: #127a45;
    --santa-red: #c8372f;
  }
  * { margin: 0; padding: 0; box-sizing: border-box; }
  html, body {
    width: 1141px;
    height: 1200px;
    overflow: hidden;
    background: var(--page);
  }
  .canvas {
    position: relative;
    width: 1141px;
    height: 1200px;
  }
  .front-sign {
    position: absolute;
    left: 30px;
    top: 438px;
    width: 1081px;
    height: 324px;
    overflow: hidden;
    background: linear-gradient(90deg, var(--sky-light) 0%, var(--sky-deep) 100%);
  }
  .snow-ground {
    position: absolute;
    inset: 0;
    width: 100%;
    height: 100%;
  }
  .headline {
    position: absolute;
    left: 34px;
    font-family: "Bebas Neue", sans-serif;
    font-size: 80px;
    line-height: 1;
    letter-spacing: 1px;
    color: var(--headline);
    white-space: nowrap;
  }
  .headline--name { top: 50px; }
  .headline--showing { top: 113px; }
  .headline .highlight { color: var(--accent-red); }
  .tagline {
    position: absolute;
    left: 44px;
    top: 212px;
    font-family: "Almendra Display", serif;
    font-size: 58px;
    line-height: 1;
    color: var(--headline);
    white-space: nowrap;
  }
  .tagline .highlight { color: var(--accent-red); }
  .festive-art {
    position: absolute;
    left: 822px;
    top: 31px;
    width: 250px;
    height: 284px;
    background: linear-gradient(160deg, var(--tree-green) 0%, var(--tree-green) 50%, var(--santa-red) 100%);
    border-radius: 6px;
    opacity: 0.9;
  }
</style>
</head>
<body>
  <main class="canvas">
    <section class="front-sign" aria-label="Shop front sign">
      <svg class="snow-ground" viewBox="0 0 1081 324" preserveAspectRatio="none" aria-hidden="true">
        <path d="M451 324 C 640 318, 880 305, 1081 292 L 1081 324 Z" fill="var(--snow)"/>
        <circle cx="606" cy="38" r="6" fill="var(--snow)"/>
        <circle cx="788" cy="35" r="6" fill="var(--snow)"/>
        <circle cx="1040" cy="125" r="7" fill="var(--snow)"/>
        <circle cx="930" cy="20" r="3" fill="var(--snow)"/>
        <circle cx="860" cy="50" r="3" fill="var(--snow)"/>
        <circle cx="985" cy="60" r="3" fill="var(--snow)"/>
        <circle cx="1055" cy="175" r="3" fill="var(--snow)"/>
        <circle cx="640" cy="60" r="2.5" fill="var(--snow)"/>
        <circle cx="700" cy="270" r="2.5" fill="var(--snow)"/>
        <circle cx="760" cy="120" r="2.5" fill="var(--snow)"/>
      </svg>

      <h1 class="headline headline--name">Penny Wise Bargain Store</h1>
      <p class="headline headline--showing">With <span class="highlight">the last 1.5m showing</span></p>
      <p class="tagline">The <span class="highlight">Xmas Shop</span> open all Year</p>

      <div class="festive-art" role="img" aria-label="Illustration of a Christmas tree, Santa riding a red sleigh and wrapped gift boxes"></div>
    </section>
  </main>
</body>
</html>
```